Tending Our Garden eBook Cover Design

I want to deisgn a cover for my eBook (FRONT COVER) and the title is:

Under the Willow Tree; Where I Found My Quiet Strength and Where You Might Too
By KT Dorran

TITLE CHANGED TO: UNDER THE WILLOW TREE; WHERE I FOUND MY QUIET STRENGTH AND WHERE YOU MIGHT TOO

The color palette is attached. Along with some photos options of me. Along with the ebook in WORD Document. My website is www.KTDorranLive.example. You can use a different color palette if you think it is best

Target Market(s)

women who look to build a personal brand

Industry/Entity Type

health and wellness

Requirements
Must have
• the title
Nice to have
• use my picture on the cover; but that is optional
Should not have
• any men

```html
<!DOCTYPE html>
<html lang="en">
<head>
<meta charset="utf-8">
<title>Under the Willow Tree — KT Dorran</title>
<link rel="stylesheet" href="https://fonts.googleapis.com/css2?family=Josefin+Sans:wght@600;700&display=swap">
<style>
  :root {
    --stage: #f3f3f3;
    --cover-ink: #05060c;
    --gold-light: #e7c77a;
    --gold: #c9982f;
    --gold-deep: #9a6e1c;
    --cream: #f1dca6;
    --portrait-red: #d8241a;
    --portrait-dark: #120d12;
  }
  * { margin: 0; padding: 0; box-sizing: border-box; }
  html, body { width: 1200px; height: 857px; overflow: hidden; background: var(--stage); }
  .canvas { position: relative; width: 1200px; height: 857px; display: flex; align-items: center; justify-content: center; }
  .cover {
    position: relative; width: 520px; height: 790px; background: var(--cover-ink);
    overflow: hidden; font-family: "Josefin Sans", sans-serif; text-align: center;
  }
  .portrait {
    position: absolute; left: 0; right: 0; bottom: 0; height: 470px;
    background:
      radial-gradient(ellipse 40% 52% at 50% 85%, var(--portrait-red) 0%, #a3180f 55%, transparent 76%),
      radial-gradient(ellipse 22% 30% at 50% 30%, #2a1a16 0%, transparent 80%),
      linear-gradient(180deg, var(--cover-ink) 0%, var(--portrait-dark) 60%, #1d0e0c 100%);
  }
  .title { position: relative; z-index: 1; padding: 28px 24px 0; white-space: nowrap; }
  .title-lead, .title-tail { display: block; color: var(--cream); font-weight: 700; letter-spacing: 0.5px; line-height: 1.15; }
  .title-lead { font-size: 31px; }
  .title-mid, .title-key {
    display: block; font-weight: 700; text-transform: uppercase; line-height: 1;
    background: linear-gradient(180deg, var(--gold-light), var(--gold) 55%, var(--gold-deep));
    -webkit-background-clip: text; background-clip: text; color: transparent;
  }
  .title-mid { font-size: 52px; letter-spacing: 6px; margin-top: 8px; }
  .title-key { font-size: 76px; letter-spacing: 4px; margin-top: 6px; }
  .title-tail { font-size: 29px; margin-top: 10px; }
  .byline {
    position: absolute; left: 0; right: 0; bottom: 24px; z-index: 1;
    color: var(--cream); font-size: 44px; font-weight: 700; letter-spacing: 1px; white-space: nowrap;
  }
</style>
</head>
<body>
  <div class="canvas">
    <div class="cover">
      <div class="portrait" role="img" aria-label="Portrait photo of the author in a red dress seated in a director's chair against a dark studio backdrop"></div>
      <h1 class="title">
        <span class="title-lead">UNDER THE WILLOW TREE;</span>
        <span class="title-lead">WHERE I FOUND MY</span>
        <span class="title-mid">QUIET</span>
        <span class="title-key">STRENGTH</span>
        <span class="title-tail">AND WHERE YOU MIGHT TOO</span>
      </h1>
      <p class="byline">BY KT DORRAN</p>
    </div>
  </div>
</body>
</html>
```